TAVRO Capital Group LLC a High Risk Big Rewards company for Rich Young Entrepreneurs

We would like a very modern, powerful in the eyes of our customers, modern, minimalist feel, financial gain. this business card is for young Rich entrepreneurs who want to invest money into High Risk, Big Rewards Businesses. The card Should sell the business!! let your creativity go Wild! I pick most of the designers for this project because of your BOLD Designs, I would like this card to be Bold, Modern, Minimalist, use as many effects in your graphic Artist Mind, Do not let the Financial sound of this business to make you think Conservative that's the last thing we are! if you have a lot of money and you want to play a risky market call US
Updates

Project Deadline Extended
Reason: have not received, enough designs to choose 1st and second place, sure I have received over 100 designs but it seems most designers are submitting every card they have ever made before and calling it mine, please we are looking for fresh ideas please!

Target Market(s)

Private Risky Investors

Industry/Entity Type

Financial

Contact Information for Business Card

powerful in the eyes of our customers,modern, minimalist feel

Font styles to use
Other font styles liked:
• Modern feeling fonts

Requirements
Must have
• The Company Name is TAVRO Capital Group LLC and it must be on the CARD
• My Name, title, Cell , email
• Delvin Ashcroft G.E.D.
• Managing Member
• 555.038.6195
• delvin@tavrocapitalgroup.example
Nice to have
• try a black thick plastic card with round corners with Delvin Ashcroft GED (make sure GED is smaller than name) just on one side of the card, and my phone number with out the icons and email on the other side, this card should look like a exclusive credit card or exclusive VIP card, something you would never loose

```html
<!DOCTYPE html>
<html lang="en">
<head>
<meta charset="utf-8">
<title>TAVRO Capital Group LLC – Business Card</title>
<link rel="stylesheet" href="https://fonts.googleapis.com/css2?family=Ubuntu:wght@300;400&display=swap">
<style>
  :root {
    --page-bg: #ffffff;
    --card-navy: #4a5270;
    --card-slate: #2c3140;
    --card-black: #030405;
    --band-silver-dark: #b9b9bb;
    --band-silver-light: #e6e6e8;
    --band-text: #2a2b31;
    --wordmark: #c9c9cd;
  }
  html, body {
    margin: 0;
    padding: 0;
    width: 1200px;
    height: 801px;
    overflow: hidden;
    background: var(--page-bg);
  }
  .canvas {
    position: relative;
    width: 1200px;
    height: 801px;
    font-family: "Ubuntu", "Helvetica Neue", Arial, sans-serif;
  }
  .card {
    position: absolute;
    left: 58px;
    top: 83px;
    width: 1087px;
    height: 637px;
    border-radius: 52px;
    overflow: hidden;
    background:
      linear-gradient(158deg,
        var(--card-navy) 0%,
        var(--card-navy) 22%,
        var(--card-slate) 52%,
        var(--card-black) 82%,
        var(--card-black) 100%);
  }
  .card__band {
    position: absolute;
    left: 0;
    top: 285px;
    width: 100%;
    height: 127px;
    background: linear-gradient(90deg,
      var(--band-silver-dark) 0%,
      #d4d4d6 20%,
      var(--band-silver-dark) 45%,
      #d0d0d2 65%,
      var(--band-silver-light) 82%,
      var(--band-silver-dark) 100%);
    display: flex;
    align-items: center;
    justify-content: center;
  }
  .card__email {
    color: var(--band-text);
    font-weight: 300;
    font-size: 35px;
    letter-spacing: 0.2px;
    margin-left: -8px;
  }
  .card__wordmark {
    position: absolute;
    right: 76px;
    top: 430px;
    margin: 0;
    color: var(--wordmark);
    font-weight: 300;
    font-size: 118px;
    line-height: 1;
    letter-spacing: 2px;
  }
</style>
</head>
<body>
  <main class="canvas">
    <section class="card" aria-label="TAVRO Capital Group LLC business card">
      <div class="card__band">
        <span class="card__email">delvin@tavrocapitalgroup.example</span>
      </div>
      <p class="card__wordmark">TAVRO</p>
    </section>
  </main>
</body>
</html>
```